Bright Harbor Counseling Letterhead for hip modern business

I would like some ombre use of the colors in the logo hip letterhead that incorporates logo colors and feel, needs to connect with young professionals and college students. i need to be able to write letters to schools to excuse absences as well. i like color blocks on one side preferably using colors from the attached logo design.

Target Market(s)

high income young people, young adults and college students

Industry/Entity Type

mental health

Font styles to use
Serif
Sans Serif

Colors
0054AA
0677BA
7BADD7
CADEEF
E8F1F8
0094D4
00A9DD
6FCCEA
C7EBF8
E9F6FB
00AB8E
00BBA5
67D7C9
C6EFE9
E9F9F6
59FF00
82FF00
B8FF75
E3FFCB
F4FFEA
A7469A
B969AE
D3A5CF
EDDBEB
F8F0F9
6B429C
8869AF
B7A5CE
E3DAEB
F3F0F8

Requirements
Must have
• a modern hip feel, somewhat color

```html
<!DOCTYPE html>
<html lang="en">
<head>
<meta charset="utf-8">
<title>Bright Harbor Counseling Letterhead</title>
<link href="https://fonts.googleapis.com/css2?family=Jost:wght@300;400;600&display=swap" rel="stylesheet">
<style>
  :root {
    --paper: #ececec;
    --paper-light: #f6f6f6;
    --ink: #1e1e1e;
    --teal: #2d8c9c;
    --sky: #c2dfea;
    --mint: #bcdcd8;
    --blue-soft: #b2c6dc;
    --lilac: #c6b6d8;
    --rose: #dbb9cb;
  }
  * { margin: 0; padding: 0; box-sizing: border-box; }
  html, body { width: 960px; height: 1200px; overflow: hidden; }
  body { font-family: "Jost", sans-serif; color: var(--ink); background: var(--paper); }
  .letterhead {
    position: relative; width: 960px; height: 1200px; overflow: hidden;
    background: linear-gradient(100deg, var(--paper-light) 0%, var(--paper) 55%, #e2e2e2 100%);
  }
  .brand { position: absolute; left: 65px; top: 108px; display: flex; align-items: flex-start; gap: 12px; }
  .brand-mark { width: 22px; height: 22px; border-radius: 50%; background: var(--teal); margin-top: 10px; }
  .brand-name { font-weight: 300; color: var(--ink); line-height: 1.05; }
  .brand-name .primary { display: block; font-size: 38px; letter-spacing: 0.5px; }
  .brand-name .secondary { display: block; font-size: 21px; letter-spacing: 3px; text-align: right; margin-top: 2px; }
  .contact { position: absolute; right: 107px; top: 84px; text-align: right; font-size: 15px; line-height: 18px; font-weight: 400; font-style: normal; }
  .contact .company { color: var(--teal); font-weight: 600; }
  .contact .lines { margin-top: 18px; }
  .contact .label { color: var(--teal); font-weight: 600; margin-right: 3px; }
  .contact .site { color: var(--teal); font-weight: 600; margin-top: 14px; }
  .salutation { position: absolute; left: 65px; top: 358px; font-size: 22px; font-weight: 400; }
  .body-copy { position: absolute; left: 65px; top: 423px; width: 788px; font-size: 13.4px; line-height: 18.4px; font-weight: 300; text-align: justify; }
  .body-copy p + p { margin-top: 18.4px; }
  .closing { position: absolute; left: 65px; top: 806px; font-size: 13.4px; font-weight: 300; }
  .signature { position: absolute; left: 86px; top: 846px; width: 124px; height: 66px; background: linear-gradient(90deg, #dedede, #e6e6e6); border-radius: 4px; }
  .backdrop {
    position: absolute; left: 0; bottom: 0; width: 960px; height: 300px;
    background: linear-gradient(90deg,
      rgba(194,223,234,0) 0%,
      var(--sky) 14%,
      var(--sky) 34%,
      var(--mint) 48%,
      var(--blue-soft) 62%,
      var(--lilac) 78%,
      var(--rose) 92%,
      var(--rose) 100%);
    -webkit-mask-image: linear-gradient(to bottom, transparent 0%, rgba(0,0,0,0.85) 45%, #000 100%);
            mask-image: linear-gradient(to bottom, transparent 0%, rgba(0,0,0,0.85) 45%, #000 100%);
  }
</style>
</head>
<body>
<main class="letterhead">
  <header>
    <div class="brand">
      <span class="brand-mark"></span>
      <div class="brand-name">
        <span class="primary">Bright Harbor</span>
        <span class="secondary">Counseling</span>
      </div>
    </div>
    <address class="contact">
      <div class="company">BRIGHT HARBOR LLC</div>
      <div>2140 Lantern</div>
      <div>Way Juneau</div>
      <div>Alaska 99801</div>
      <div class="lines">
        <div><span class="label">T</span>: 555-014-2230</div>
        <div><span class="label">C</span>: 555-014-7781</div>
        <div><span class="label">F</span>: 555-014-3906</div>
        <div><span class="label">E</span>: hello@brightharbor.example</div>
      </div>
      <div class="site">brightharbor.example</div>
    </address>
  </header>

  <h1 class="salutation">Dear Mr. Carter,</h1>

  <section class="body-copy">
    <p>Lorem ipsum dolor sit amet, consectetur adipiscing elit. Donec orci purus, luctus vitae dignissim eu, iaculis sed purus. Vivamus faucibus, ipsum nec aliquet viverra, leo mauris condimentum ligula, sit amet sagittis enim ligula quis arcu. Nam egestas tortor id nisi porttitor mattis. In tortor ante, ultricies in suscipit a, tempus non massa. Vivamus et auctor mi. Fusce vel massa nulla. Phasellus nec eros mauris, et scelerisque orci.</p>
    <p>Donec malesuada orci vitae nulla accumsan porta a id massa. Quisque accumsan iaculis magna sit amet fringilla. Maecenas consequat, magna eget tincidunt semper, odio nibh rutrum mi, id feugiat ante nisi eu risus. Vestibulum nunc orci, rhoncus a placerat in, ultricies in mi. Cras mattis varius eros, vel fringilla nisi suscipit eget. Quisque scelerisque sagittis nulla at porttitor.</p>
    <p>Sed id augue vitae urna euismod commodo aliquet a quam. Pellentesque arcu velit, cursus et malesuada ut, consequat et diam. Nullam erat sem, rhoncus id ullamcorper vitae, rhoncus et arcu. In ultricies ultricies nulla, ut rutrum nisi iaculis at. Donec eu magna a metus ornare faucibus. Fusce aliquet faucibus ultricies. Morbi semper, est id tincidunt gravida, sem arcu adipiscing lacus, ac bibendum nulla leo eu purus. Quisque nec diam sed risus consectetur a ccumsan quis quis nibh. Vestibulum id purus lorem.</p>
    <p>It is a long established fact that a reader will be distracted by the readable content of a page when looking at its layout. The point of using Lorem Ipsum is that it has a more-or-less normal distribution of letters, as opposed to using 'Content here, content here', making it look like readable English. Many desktop publishing packages</p>
  </section>

  <p class="closing">Sincerely,</p>
  <div class="signature" role="img" aria-label="Handwritten signature of the sender"></div>

  <div class="backdrop" role="img" aria-label="Soft pastel colour field in sky blue, mint, lilac and rose along the bottom of the page"></div>
</main>
</body>
</html>
```